Concepts needed for Brochure design

Hi,

Looking for professional brochure design concepts to present our company's Training & Business Consultancy abilities as detailed and included in the 12 slide PowerPoint presentation.
Need to include all the information in the presentation, so looking at creative concept options to present this in a professional 4 page brochure with related images and color palette that matches our website www.ruvko.com.
Thanks,
Brent.

```html
<!DOCTYPE html>
<html lang="en">
<head>
<meta charset="utf-8">
<title>RVK Training &amp; Consultancy</title>
<link href="https://fonts.googleapis.com/css2?family=Open+Sans:wght@700;800&family=PT+Sans:wght@400;700&display=swap" rel="stylesheet">
<style>
:root{
  --teal:#1f7489;
  --teal-dark:#1a5a6b;
  --hex:#184f60;
  --hex-core:#1b2450;
  --navy:#1c2c50;
  --orange:#ef8a1d;
  --white:#ffffff;
}
*{margin:0;padding:0;box-sizing:border-box}
html,body{width:848px;height:1200px;overflow:hidden;background:var(--white)}
.page{position:relative;width:848px;height:1200px;overflow:hidden;font-family:"PT Sans",Arial,sans-serif;color:var(--navy)}
.backdrop{position:absolute;left:0;top:0}
.block{position:absolute}
.title{font-family:"Open Sans",Arial,sans-serif;font-weight:800;letter-spacing:.5px;line-height:1}
.intro-title{left:28px;top:22px;font-size:56px;color:var(--white)}
.brand{position:absolute;right:34px;top:36px;display:flex;align-items:center;gap:8px;font-family:"Open Sans",Arial,sans-serif;font-weight:800;font-size:30px;color:var(--white)}
.brand-dot{width:18px;height:18px;border-radius:50%;background:var(--orange)}
.intro-text{color:var(--white);font-size:10.8px;line-height:1.4}
.intro-text p{margin-bottom:12px}
.intro-text p:last-child{margin-bottom:0}
.intro-left{left:28px;top:110px;width:386px}
.intro-right{left:435px;top:110px;width:393px}
.section-title{color:var(--navy);font-size:38px}
.vvm-title{left:26px;top:354px}
.core-title{left:26px;top:534px}
.col-head{font-family:"Open Sans",Arial,sans-serif;font-weight:700;color:var(--orange);font-size:20px;line-height:1;margin-bottom:5px}
.col-text{font-size:11.2px;line-height:1.4;color:var(--navy)}
.justify{text-align:justify}
.vision{left:26px;top:405px;width:262px}
.values{left:299px;top:405px;width:258px}
.mission{left:572px;top:405px;width:255px}
.consult{left:26px;top:577px;width:262px}
.training{left:299px;top:577px;width:258px}
.csat{left:572px;top:577px;width:255px}
.consult .col-head{padding-left:4px}
.solutions-title{left:36px;top:820px;color:var(--white);font-size:36px}
.sol-list{position:absolute;list-style:none;color:var(--white);font-size:11.6px;line-height:1.45}
.sol-list li{position:relative;padding-left:11px}
.sol-list li::before{content:"";position:absolute;left:0;top:7px;width:3px;height:3px;border-radius:50%;background:var(--white)}
.l1{left:50px;top:893px;width:190px}
.l2{left:50px;top:978px;width:190px}
.l3{left:50px;top:1080px;width:190px}
.r1{left:612px;top:893px;width:200px}
.r2{left:612px;top:978px;width:200px}
.r3{left:612px;top:1080px;width:200px}
.hex-label{font-family:"PT Sans",Arial,sans-serif;font-size:14px;fill:var(--white);text-anchor:middle}
.hex-core-label{font-family:"Open Sans",Arial,sans-serif;font-weight:800;font-size:22px;fill:var(--white);text-anchor:middle}
</style>
</head>
<body>
<main class="page">
  <svg class="backdrop" width="848" height="1200" viewBox="0 0 848 1200">
    <defs>
      <polygon id="hex" points="0,-54 46.8,-27 46.8,27 0,54 -46.8,27 -46.8,-27"/>
    </defs>
    <path d="M0 0H848V346C780 338 680 326 560 330C420 335 300 350 170 344C100 341 40 334 0 332Z" fill="var(--teal)"/>
    <path d="M0 812C110 795 200 770 330 778C460 786 560 805 680 792C760 784 810 770 848 762V1200H0Z" fill="var(--teal)"/>
    <g stroke="var(--white)" stroke-width="2">
      <line x1="236" y1="929" x2="298" y2="929"/>
      <line x1="537" y1="929" x2="598" y2="929"/>
      <line x1="578" y1="1007" x2="598" y2="1007"/>
      <line x1="226" y1="1089" x2="300" y2="1089"/>
      <line x1="530" y1="1089" x2="598" y2="1089"/>
    </g>
    <g fill="var(--hex)">
      <use href="#hex" x="360" y="929"/>
      <use href="#hex" x="469" y="929"/>
      <use href="#hex" x="305" y="1008"/>
      <use href="#hex" x="524" y="1008"/>
      <use href="#hex" x="360" y="1087"/>
      <use href="#hex" x="469" y="1087"/>
    </g>
    <use href="#hex" x="415" y="1008" fill="var(--hex-core)"/>
    <text class="hex-label" x="360" y="934">Customer</text>
    <text class="hex-label" x="469" y="934">Productivity</text>
    <text class="hex-label" x="305" y="1004">Business</text>
    <text class="hex-label" x="305" y="1022">Analysis</text>
    <text class="hex-label" x="524" y="1013">Compliance</text>
    <text class="hex-label" x="360" y="1092">Cycle Time</text>
    <text class="hex-label" x="469" y="1092">Visibility</text>
    <text class="hex-core-label" x="415" y="1016">RVK</text>
  </svg>

  <h1 class="block title intro-title">Introduction</h1>
  <div class="brand"><span class="brand-dot"></span>RVK</div>

  <div class="block intro-text intro-left">
    <p>R.V.K (Results Value Kaizen) Training &amp; Consultancy is a premier Business Consultancy &amp; Corporate Training Firm setup in Perth, Western Australia since early 2013.</p>
    <p>We are specialised in Strategic Business Improvement Programs and have been providing best-in-class and internationally accredited Lean Six Sigma Training and Business &amp; Process Improvement consultancy services and Project Management solutions to Professionals and Organisations across Australia &amp; Asia-Pacific Region.</p>
    <p>RVKTC was setup in early 2013 by a group of certified, experienced and passionate Lean Six Sigma professionals &amp; Senior Business Consultants who have successfully engaged &amp; implemented large scale Business transformation, Process Re-Engineering Programs &amp; Improvement initiatives in both Production</p>
  </div>
  <div class="block intro-text intro-right">
    <p>/ Manufacturing &amp; Service oriented industries in some of Australia's largest businesses like Redstone Iron Ore, The Coastline Financial Group, Norikawa Australia and other global Industry leaders in Finance, BPO, Logistics across Asia, Europe &amp; North America as well</p>
    <p>Through our global network of business partners spanning over 4 continents and our team of highly competent and experienced Business Improvement Principals, Consultants and Professionals, we provide services that offer Value creation and enable Innovation and Sustainability by mirroring global best business practices and implementing advanced improvement methodologies to eliminate waste and decrease variation and increase customer satisfaction in their products and services.</p>
  </div>

  <h2 class="block title section-title vvm-title">Vision, Values, Missions</h2>
  <section class="block vision">
    <h3 class="col-head">Vision</h3>
    <p class="col-text">To be an globally recognized provider of world class training and consulting services displaying high level of intelligence and integrity to add value to our clients by adding immense value to their business.</p>
  </section>
  <section class="block values">
    <h3 class="col-head">Values</h3>
    <p class="col-text">The cornerstones of our business are QUALITY, INNOVATION, EXPERIENCE and EXCELLENCE. Our values and culture are based on providing our customer with the best possible solutions, leading edge resources, and a passion for excellence.</p>
  </section>
  <section class="block mission">
    <h3 class="col-head">Mission</h3>
    <p class="col-text">"Exceed expectations consistently, by creating value for our customers and enabling innovation &amp; excellence"</p>
  </section>

  <h2 class="block title section-title core-title">Core Services</h2>
  <section class="block consult">
    <h3 class="col-head">Consultancy</h3>
    <p class="col-text justify">Through Our team and network of highly competent and experienced Business improvement professionals, we provide Business Consultancy services that offer Value creation and enable Innovation and Sustainability by mirroring global best business practices and implementing advanced improvement methodologies to eliminate waste and decrease variation and increase customer satisfaction in their products and services.</p>
  </section>
  <section class="block training">
    <h3 class="col-head">Training</h3>
    <p class="col-text justify">What sets our program apart from others is our focus on providing extremely intuitive, interactive and engaging training material. Accredited by multiple global bodies including ILSCB and QSB our online training platform and curriculum, is one of the worlds best for Business improvement training and is used by leading enterprises, government entities and universities to increase training impact and reduce training time, costs, and disruption.</p>
  </section>
  <section class="block csat">
    <h3 class="col-head">C-Sat Surveys &amp; Analysis</h3>
    <p class="col-text justify">Our team of experienced Specialists and Business Analysts help you understand your customers well by measuring customer sentiments, customer effort and loyalty using well established methods of Customer Satisfaction research and Mystery Shopping Insights.</p>
  </section>

  <h2 class="block title solutions-title">Business Consultancy Solutions</h2>
  <ul class="sol-list l1">
    <li>VOC to CTQ Analysis</li>
    <li>Improvements of CTQ</li>
    <li>Build methodology to conduct Mystery shopping insights</li>
  </ul>
  <ul class="sol-list l2">
    <li>Requirements Management</li>
    <li>BA CoE Setup</li>
    <li>Change Impact Analysis</li>
  </ul>
  <ul class="sol-list l3">
    <li>Process Analysis</li>
    <li>Simulation</li>
    <li>VSM</li>
    <li>Eliminate inefficiency</li>
    <li>Decrease handoff and bottlenecks</li>
  </ul>
  <ul class="sol-list r1">
    <li>Automated process execution across IT systems and people</li>
    <li>Reduce manual hand-offs, errors and bottlenecks.</li>
  </ul>
  <ul class="sol-list r2">
    <li>Identify Requirements</li>
    <li>Create Process Breakdown Structure (PBS)</li>
    <li>Integration of the PBS within the Process</li>
  </ul>
  <ul class="sol-list r3">
    <li>Business Modeling</li>
    <li>SOPs</li>
    <li>Assessment Documents</li>
    <li>Governance</li>
    <li>Exceptions Documentation</li>
  </ul>
</main>
</body>
</html>
```